Financial Planner Letterhead + Business Card

We need letterhead and business card designed for a financial advisory firm. The letterhead and business card should make use of our existing logo, and colors should be similar to logo...which is attached. we want to communicate safety, trust, stability. We need the ability to edit the final files so that we can add additional phone number

Both the letterhead and business card MUST contain the following disclosure: Most of the samples so far did not follow this instruction.

Securities and advisory services offered through Harborview Capital Alliance®, member BXQMA/TOLV, a Registered Investment Adviser. Fixed insurance products and services offered through DRW Insurance Agency

details
Tessa Marlow
President & Wealth Advisor
812 E. 9th Street, Suite 6
Corsicana, TX 75391
903-512-0948
Tessa@lumenrw.example
web: www.lumenridgewealth.example

Target Market(s)

all adults - primary those 50 and older, generally college degreed professionals

Industry/Entity Type

Business

Contact Information for Business Card

must include this disclosure:
Securities and advisory services offered through Harborview Capital Alliance®, member BXQMA/TOLV, a Registered Investment Adviser

details
Tessa Marlow
Corsicana, TX 75391
903-512-0948
Tessa@lumenrw.example

Font styles to use
Sans Serif

Colors

Designer to choose colors to be used in the design.

Requirements
Must have
• logo, name/address info
• appealing visually, stands out without being overwhelming
• MUST HAVE DISCLOSURE !! (in footer of letterhead & on back of business card).
• Securities and advisory services offered through Harborview Capital Alliance®, member BXQMA/TOLV, a Registered Investment Adviser. Fixed insurance products and services offered through DRW Insurance Agency
Should not have
• lines indicating upward movement (such as up arrows)

```html
<!DOCTYPE html>
<html lang="en">
<head>
<meta charset="utf-8">
<title>Lumenridge Wealth — Letterhead and Business Card</title>
<link href="https://fonts.googleapis.com/css2?family=Open+Sans:wght@400;600;700&display=swap" rel="stylesheet">
<style>
  :root {
    --backdrop: #efefef;
    --paper: #ffffff;
    --navy: #1f3d7a;
    --blue: #2496d0;
    --green: #6cb33f;
    --ink: #333333;
    --muted: #6b6b6b;
    --rule: #7dbb4a;
  }
  * { margin: 0; padding: 0; box-sizing: border-box; }
  html, body { width: 1200px; height: 1200px; overflow: hidden; background: var(--backdrop); }
  body { font-family: "Open Sans", Arial, sans-serif; color: var(--ink); position: relative; }

  .letterhead {
    position: absolute; left: 106px; top: 180px; width: 630px; height: 830px;
    background: var(--paper);
  }
  .brand { position: absolute; display: flex; flex-direction: column; align-items: center; }
  .brand-mark { background: var(--green); }
  .brand-name { font-weight: 600; color: var(--navy); white-space: nowrap; }

  .letterhead .brand { left: 40px; top: 48px; width: 130px; }
  .letterhead .brand-mark { width: 48px; height: 48px; margin-bottom: 10px; }
  .letterhead .brand-name { font-size: 17px; }

  .contact { position: absolute; border-left: 1.5px solid var(--rule); }
  .contact p { line-height: 1.15; white-space: nowrap; }
  .contact .row { display: flex; align-items: center; gap: 4px; }
  .contact svg { flex: none; }

  .letterhead .contact { left: 427px; top: 64px; height: 65px; padding-left: 13px; font-size: 10px; }
  .letterhead .contact .address { margin-bottom: 9px; }
  .letterhead .contact .row { margin-bottom: 2px; }

  .disclosure { position: absolute; text-align: center; line-height: 1.45; }
  .letterhead .disclosure {
    left: 50px; right: 50px; bottom: 28px; padding-top: 10px;
    border-top: 1px solid var(--rule); font-size: 8px; color: var(--muted);
  }

  .card { position: absolute; left: 810px; width: 292px; }
  .card-front { top: 182px; height: 173px; background: var(--paper); }
  .card-front .brand { left: 18px; top: 50px; width: 122px; }
  .card-front .brand-mark { width: 40px; height: 40px; margin-bottom: 9px; }
  .card-front .brand-name { font-size: 12px; }
  .card-front .contact { left: 150px; top: 49px; height: 76px; padding-left: 11px; font-size: 6.6px; }
  .card-front .holder { font-size: 10.5px; font-weight: 700; color: var(--green); line-height: 1.1; }
  .card-front .role { margin-bottom: 8px; }
  .card-front .address { margin-bottom: 7px; }
  .card-front .row { margin-bottom: 2px; }

  .card-back {
    top: 405px; height: 169px;
    background: linear-gradient(90deg, #243a76 0%, #1f5b99 50%, var(--blue) 100%);
  }
  .card-back .brand { left: 0; right: 0; top: 38px; }
  .card-back .brand-mark { width: 48px; height: 48px; margin-bottom: 12px; }
  .card-back .brand-name { font-size: 19px; color: #ffffff; }
  .card-back .disclosure {
    left: 24px; right: 24px; bottom: 12px; font-size: 5.8px; color: rgba(255,255,255,0.85);
  }
</style>
</head>
<body>

<section class="letterhead">
  <div class="brand">
    <div class="brand-mark"></div>
    <div class="brand-name">Lumenridge Wealth</div>
  </div>
  <div class="contact">
    <p class="address">812 E. 9th Street, Suite 6<br>Corsicana, TX 75391</p>
    <p class="row">
      <svg width="8" height="8" viewBox="0 0 10 10"><path d="M2 1 L4 3 L3 4.5 Q4.5 6.5 5.5 7 L7 6 L9 8 L7.5 9.5 Q3 8.5 0.5 2.5 Z" fill="var(--navy)"/></svg>
      903-512-0948</p>
    <p class="row">
      <svg width="8" height="6" viewBox="0 0 10 7"><rect width="10" height="7" fill="var(--navy)"/><path d="M0 0 L5 4 L10 0" stroke="#fff" fill="none"/></svg>
      Tessa@lumenrw.example</p>
    <p class="row">
      <svg width="8" height="8" viewBox="0 0 10 10"><circle cx="5" cy="5" r="4.3" stroke="var(--navy)" fill="none"/><path d="M0.7 5 H9.3 M5 0.7 V9.3" stroke="var(--navy)"/></svg>
      www.lumenridgewealth.example</p>
  </div>
  <p class="disclosure">Securities and advisory services offered through Harborview Capital Alliance®, member BXQMA/TOLV, a Registered Investment Adviser.<br>Fixed insurance products and services offered through DRW Insurance Agency</p>
</section>

<section class="card card-front">
  <div class="brand">
    <div class="brand-mark"></div>
    <div class="brand-name">Lumenridge Wealth</div>
  </div>
  <div class="contact">
    <p class="holder">Tessa Marlow</p>
    <p class="role">President &amp; Wealth Advisor</p>
    <p class="address">812 E. 9th Street, Suite 6<br>Corsicana, TX 75391</p>
    <p class="row">
      <svg width="6" height="6" viewBox="0 0 10 10"><path d="M2 1 L4 3 L3 4.5 Q4.5 6.5 5.5 7 L7 6 L9 8 L7.5 9.5 Q3 8.5 0.5 2.5 Z" fill="var(--green)"/></svg>
      903-512-0948</p>
    <p class="row">
      <svg width="6" height="5" viewBox="0 0 10 7"><rect width="10" height="7" fill="var(--green)"/><path d="M0 0 L5 4 L10 0" stroke="#fff" fill="none"/></svg>
      Tessa@lumenrw.example</p>
    <p class="row">
      <svg width="6" height="6" viewBox="0 0 10 10"><circle cx="5" cy="5" r="4.3" stroke="var(--green)" fill="none"/><path d="M0.7 5 H9.3 M5 0.7 V9.3" stroke="var(--green)"/></svg>
      www.lumenridgewealth.example</p>
  </div>
</section>

<section class="card card-back">
  <div class="brand">
    <div class="brand-mark"></div>
    <div class="brand-name">Lumenridge Wealth</div>
  </div>
  <p class="disclosure">Securities and advisory services offered through Harborview Capital Alliance®,<br>member BXQMA/TOLV, a Registered Investment Adviser</p>
</section>

</body>
</html>
```